Brivelle drinking water Label.

I want Drinking water label that stands out from the rest..Elegant Attractive and visible label design. Brand name is 'BRIVELLE'.

Target Market(s)

KENYA.

Industry/Entity Type

Water Company

Requirements
Must have
• Must be unique. Must be elegant and have vibrant and eye catching color.
Nice to have
• Clear or colored background with water like effects.
Should not have
• Should not have more that 4 colors.

```html
<!DOCTYPE html>
<html lang="en">
<head>
<meta charset="utf-8">
<title>Brivelle Drinking Water Label</title>
<link rel="stylesheet" href="https://fonts.googleapis.com/css2?family=Cinzel:wght@400;500&family=Open+Sans:wght@400&family=PT+Serif&display=swap">
<style>
  :root {
    --backdrop: #a7d2ea;
    --label-white: #f5f8f9;
    --brand-blue: #2f6ec0;
    --mineral-green: #4fae46;
    --wave-cyan: #3bb6da;
    --wave-deep: #2f8fd0;
  }
  html, body {
    margin: 0;
    padding: 0;
    width: 1187px;
    height: 1200px;
    overflow: hidden;
    background: var(--backdrop);
  }
  .canvas {
    position: relative;
    width: 1187px;
    height: 1200px;
  }
  .label {
    position: absolute;
    left: 214px;
    top: 60px;
    width: 760px;
    height: 1080px;
    background: var(--label-white);
    overflow: hidden;
    text-align: center;
  }
  .brand-name {
    position: absolute;
    left: 0;
    right: 0;
    top: 170px;
    margin: 0;
    font-family: "Cinzel", serif;
    font-weight: 400;
    font-size: 132px;
    line-height: 1;
    letter-spacing: 4px;
    color: var(--brand-blue);
  }
  .tagline {
    position: absolute;
    left: 0;
    right: 0;
    top: 460px;
    margin: 0;
    font-family: "Cinzel", serif;
    font-weight: 500;
    font-size: 33px;
    letter-spacing: 1px;
    color: var(--mineral-green);
  }
  .drop-icon {
    position: absolute;
    left: 338px;
    top: 530px;
    width: 84px;
    height: 120px;
  }
  .net-quantity {
    position: absolute;
    left: 0;
    right: 0;
    top: 672px;
    margin: 0;
    font-family: "Open Sans", sans-serif;
    font-size: 19px;
    color: var(--mineral-green);
  }
  .volume {
    position: absolute;
    left: 0;
    right: 0;
    top: 700px;
    margin: 0;
    font-family: "PT Serif", serif;
    font-size: 30px;
    color: var(--mineral-green);
  }
  .wave-band {
    position: absolute;
    left: 0;
    right: 0;
    top: 745px;
    bottom: 0;
    background: linear-gradient(180deg, #bfe6f2 0%, var(--wave-cyan) 45%, var(--wave-deep) 100%);
  }
</style>
</head>
<body>
  <div class="canvas">
    <section class="label">
      <h1 class="brand-name">BRIVELLE</h1>
      <p class="tagline">WATER WITH ADDED MINERALS</p>
      <svg class="drop-icon" viewBox="0 0 84 120" aria-hidden="true">
        <defs>
          <radialGradient id="drop-fill" cx="0.4" cy="0.65" r="0.6">
            <stop offset="0" stop-color="#e8f6fc"/>
            <stop offset="1" stop-color="#3b9fd0"/>
          </radialGradient>
        </defs>
        <path d="M42 4 C36 30 6 58 6 82 A36 36 0 0 0 78 82 C78 58 48 30 42 4 Z" fill="url(#drop-fill)"/>
      </svg>
      <p class="net-quantity">Net Quantity</p>
      <p class="volume">500 ml.</p>
      <div class="wave-band" role="img" aria-label="Stylised blue ocean wave pattern"></div>
    </section>
  </div>
</body>
</html>
```